Bright Current Electrical & Communications business card design

We would like a double sided business card that is different. Want it to be exciting and fun. Something that people keep rather then just throw it in the bin.
We have a logo that we want to put on one side of the business card and then the business information on the reverse side. Trying to go for a real professional style of business card

Target Market(s)

Electrical

Industry/Entity Type

Electrical

Contact Information for Business Card

Bright Current Electrical & Communications
Marcus Holloway
P: 0437 862 305
E: brightcurrent@mailbox-example.com.au
Lic No: 574106K
24/7

Font styles to use
Other font styles liked:
• Would like ideas

Requirements
Must have
• Our company logo (preferably on both sides) yellow needs to be incorporated somewhere. Business card card colours to match with logo. Maybe a small pop of colour
Nice to have
• Open to some design ideas

```html
<!DOCTYPE html>
<html lang="en">
<head>
<meta charset="utf-8">
<title>Bright Current Electrical &amp; Communications – Business Card</title>
<link rel="stylesheet" href="https://fonts.googleapis.com/css2?family=Montserrat:wght@600;700&family=Open+Sans:ital,wght@0,400;1,400&display=swap">
<style>
  :root {
    --backdrop: #a3a2a3;
    --card-dark: #111111;
    --card-light: #fbfbfa;
    --brand-grey: #6e6e6e;
    --brand-silver: #d6d6d6;
    --accent-yellow: #e6c21a;
    --ink: #1c1c1c;
    --ink-muted: #7a7a7a;
  }
  * { margin: 0; padding: 0; box-sizing: border-box; }
  html, body {
    width: 1200px; height: 1200px; overflow: hidden;
    background: var(--backdrop);
  }
  .canvas { position: relative; width: 1200px; height: 1200px; }

  .card {
    position: absolute;
    border-radius: 24px;
  }
  .card--front {
    left: 238px; top: 117px; width: 714px; height: 420px;
    background: var(--card-dark);
    display: flex; align-items: center; justify-content: center;
  }
  .card--back {
    left: 230px; top: 644px; width: 712px; height: 417px;
    background: var(--card-light);
  }

  .brand {
    display: flex; align-items: center; gap: 16px;
  }
  .brand__mark {
    flex: none;
    background: var(--accent-yellow);
  }
  .brand__name {
    font-family: "Montserrat", sans-serif;
    font-weight: 700;
    text-transform: uppercase;
    line-height: 1.15;
  }
  .card--front .brand__mark { width: 22px; height: 22px; }
  .card--front .brand__name {
    color: var(--brand-silver);
    font-size: 30px;
    letter-spacing: 1px;
  }

  .card--back .brand {
    position: absolute; left: 58px; top: 170px; gap: 12px;
  }
  .card--back .brand__mark { width: 14px; height: 14px; }
  .card--back .brand__name {
    color: var(--brand-grey);
    font-size: 20px;
    letter-spacing: 0.5px;
  }

  .contact {
    position: absolute; left: 386px; top: 118px;
    font-family: "Open Sans", sans-serif;
    color: var(--ink);
  }
  .contact__name {
    font-family: "Montserrat", sans-serif;
    font-weight: 600;
    font-size: 23px;
    letter-spacing: 0.3px;
  }
  .contact__role {
    font-style: italic;
    font-size: 15px;
    color: var(--ink-muted);
    margin-top: 4px;
  }
  .contact__list {
    list-style: none;
    margin-top: 38px;
    font-size: 17px;
    line-height: 27px;
  }
  .contact__item { display: flex; align-items: center; }
  .contact__icon {
    width: 18px; height: 14px; margin: 0 15px 0 0; flex: none;
    fill: var(--ink);
  }
  .contact__sep { margin: 0 12px; }
</style>
</head>
<body>
<main class="canvas">

  <section class="card card--front" aria-label="Business card front">
    <div class="brand">
      <span class="brand__mark"></span>
      <p class="brand__name">Bright Current<br>Electrical &amp; Communications</p>
    </div>
  </section>

  <section class="card card--back" aria-label="Business card back">
    <div class="brand">
      <span class="brand__mark"></span>
      <p class="brand__name">Bright Current<br>Electrical &amp;<br>Communications</p>
    </div>

    <div class="contact">
      <h1 class="contact__name">Marcus Holloway</h1>
      <p class="contact__role">Managing Director</p>
      <ul class="contact__list">
        <li class="contact__item">
          <svg class="contact__icon" viewBox="0 0 18 14" aria-hidden="true">
            <path d="M1 4 Q9 -1 17 4 L15 6 L12 4.5 L12 3 Q9 2 6 3 L6 4.5 L3 6 Z"/>
            <path d="M4 7 H14 L16 13 H2 Z"/>
          </svg>
          0437 862 305
        </li>
        <li class="contact__item">
          <svg class="contact__icon" viewBox="0 0 18 14" aria-hidden="true">
            <path d="M1 2 H17 V12 H1 Z M2.5 3.5 L9 8 L15.5 3.5" fill="none" stroke="#1c1c1c" stroke-width="1.6"/>
          </svg>
          brightcurrent@mailbox-example.com.au
        </li>
        <li class="contact__item">
          Lic No: 574106K<span class="contact__sep">|</span>24/7 Services
        </li>
      </ul>
    </div>
  </section>

</main>
</body>
</html>
```